Webdesign für Restaurant / Elif Grillstube
Zielgruppe
Wir führen ein türkisches Restaurant/Imbiss mit einem Catering Service und Lieferservice. Unser Betrieb ist ein 'zwischen Ding'.
Sie können es sich wie ein türkisches 'Morgenpost' oder 'Bistro Lunara' vorstellen.
Wir haben Sitzplätze und Laufkundschaft.
Zielgruppe:
Jeder der gerne gutes Essen isst.
Aufgabenstellung
Unsere Webseite soll ein "Onepager" werden.
Sie sollte auch für mobil Geräte optimiert sein.
Die Internetseite soll bei dem Interessenten folgenden Eindruck hinterlassen: Dass wir wissen was wir machen, dass wir professionell arbeiten und dass sie bei uns qualitativ hochwertiges Essen bekommen.
Die folgende Seite gefällt mir sehr gut:
http://www.vomo-bistro.com
Die Funktionsweise (Auf die Menüpunkte drücken und runterscrollen) soll die gleiche, wie auf dieser Seite sein.
Was mich an dieser Seite stört:
Die Startseite(ganz oben) wirkt meiner Meinung nach etwas "lasch". Sie wirkt etwas zu grau, leblos. Zu dunkel gehalten.
Sie sollten sich trotzdem an der erwähnten Seite orientieren, da mir der Aufbau und die sonstige Gestaltung sehr gut gefällt.
Sie können sich auch an dieser Seite orientieren:
https://www.zahlwerk.com
Farben: keine konkrete Vorstellung. Sollte sich jedoch nicht mit unserem Logo beißen.
Bilder: Sie haben freie Wahl. Wenn Sie Bilder von Speisen verwenden, sollten Sie sich an
unserer Speisekarte orientieren.
Ich sende ihnen Bilder zu, die Sie nutzen können. Müssen Sie aber nicht.
Bilder sind gekauft oder selbst gemacht.
Aufbau und Elemente zu den jeweiligen Abschnitten:
- Home: Catering sollte etwas hervorgehoben werden
Unsere Telefonnummer sollte leicht zu finden sein.
Beispiel: https://www.fjordhase.de/de/
Hintergrundbild: Ansprechendes Foto von einem Gericht(Essen)
- Anschrift
- Öffnungszeiten
- Link zu unserer Facebookseite
- (Impressum hier enthalten)
- Catering
- Lieferservice
- Menu: Unsere Speisen sollten hier übersichtlich auftauchen. (Unsere Karte finden sie auf
- Getränke: Unsere Getränke sollten hier übersichtlich auftauchen
Texte zu den Menüpunkten: <..

```html
<!DOCTYPE html>
<html lang="de">
<head>
<meta charset="utf-8">
<title>Elif Grillstube – Speisekarte</title>
<link rel="stylesheet" href="https://fonts.googleapis.com/css2?family=Archivo+Black&family=Montserrat:wght@700&family=Questrial&display=swap">
<style>
:root{
  --green:#1f7a3c;
  --ink:#1a1a1a;
  --muted:#6d6d6d;
  --paper:#ffffff;
  --stage:#eeeeee;
  --line:#d6d6d6;
}
*{margin:0;padding:0;box-sizing:border-box}
html,body{width:1090px;height:1200px;overflow:hidden;background:var(--stage)}
body{font-family:"Questrial",sans-serif;color:var(--ink)}
ul{list-style:none}
.board{position:absolute;left:0;top:0;width:1830px;height:2015px;transform:scale(.5956);transform-origin:0 0}
.screen{position:absolute;background:var(--paper);overflow:hidden;box-shadow:0 0 0 1px var(--line)}
.desktop{width:875px;height:493px}
.tablet{width:403px;height:478px}
.phone{width:178px;height:290px}

/* brand */
.brand{position:absolute;text-align:center;font-family:"Montserrat",sans-serif;font-weight:700;color:var(--green)}
.brand .mark{display:block;margin:0 auto;border-radius:50%;background:var(--green)}
.desktop .brand{left:0;top:22px;width:146px;font-size:13px}
.desktop .brand .mark{width:58px;height:58px;margin-bottom:10px}
.tablet .brand{left:0;top:20px;width:117px;font-size:11px}
.tablet .brand .mark{width:46px;height:46px;margin-bottom:8px}
.phone .brand{left:0;top:6px;width:178px;font-size:7px}
.phone .brand .mark{width:22px;height:22px;margin-bottom:3px}

/* navigation */
.nav{position:absolute;text-align:center;font-family:"Montserrat",sans-serif;font-weight:700;letter-spacing:.3px}
.nav li .boxed{border:1.5px solid var(--ink);padding:0 5px}
.desktop .nav{left:0;top:152px;width:146px;font-size:10px}
.desktop .nav li{height:29px}
.tablet .nav{left:0;top:140px;width:117px;font-size:8px}
.tablet .nav li{height:24.5px}

/* contact */
.contact{position:absolute;display:flex;gap:8px}
.contact svg{flex:none}
.contact p{line-height:1.1}
.contact .nums{color:#444;margin-top:6px}
.desktop .contact{left:18px;top:387px;font-size:10px}
.tablet .contact{left:8px;top:372px;font-size:9px}
.social{position:absolute;display:flex;align-items:center}
.social .round{border-radius:50%;background:var(--ink)}
.desktop .social{left:40px;top:456px;gap:20px}
.desktop .social .round{width:22px;height:22px}
.tablet .social{left:26px;top:442px;gap:18px}
.tablet .social .round{width:21px;height:21px}

/* photo */
.photo{position:absolute}
.photo-title{position:absolute;font-family:"Archivo Black",sans-serif;color:#fff;letter-spacing:1px;text-shadow:0 1px 3px rgba(0,0,0,.35)}
.photo-title::after{content:"";display:block;background:var(--green)}
.desktop .photo{left:144px;top:15px;width:347px;height:463px}
.desktop .photo-title{left:23px;top:68px;font-size:24px}
.desktop .photo-title::after{width:48px;height:3px;margin-top:6px}
.tablet .photo{left:117px;top:13px;width:268px;height:225px}
.tablet .photo-title{left:18px;top:68px;font-size:21px}
.tablet .photo-title::after{width:44px;height:3px;margin-top:4px}
.phone .photo{left:4px;top:57px;width:171px;height:103px}
.phone .photo-title{left:16px;top:12px;font-size:13px}
.phone .photo-title::after{width:26px;height:2px;margin-top:3px}
.starters{background:linear-gradient(165deg,#3f4a22 0%,#5e6a2f 28%,#d8c9a8 45%,#8f2417 62%,#b23a22 74%,#ece6dc 100%)}
.pizza{background:linear-gradient(150deg,#6a4a32 0%,#b0562c 30%,#9c2b1c 50%,#d09a5a 72%,#7a5236 100%)}
.drinks{background:linear-gradient(100deg,#7a4420 0%,#5a0d14 30%,#a88a64 48%,#d8a23a 70%,#a55e26 100%)}

/* menu list */
.menu{position:absolute}
.menu li{margin-bottom:var(--gap)}
.menu h3{display:flex;justify-content:space-between;font-weight:400;white-space:nowrap}
.menu p{color:var(--muted)}
.desktop .menu{left:539px;width:245px}
.desktop .menu h3{font-size:12px;line-height:14px}
.desktop .menu p{font-size:8.5px;line-height:10px;margin-top:2px;width:212px}
.tablet .menu{left:134px;width:236px}
.tablet .menu h3{font-size:11px;line-height:13px}
.tablet .menu p{font-size:8px;line-height:9.5px;margin-top:2px;width:205px}
.phone .menu{left:18px;width:144px}
.phone .menu h3{font-size:6px;line-height:7px}
.phone .menu p{font-size:4.2px;line-height:5px;margin-top:1px;width:120px}

/* right rail */
.section-label{position:absolute;writing-mode:vertical-rl;color:var(--muted);letter-spacing:.3px}
.desktop .section-label{right:12px;top:20px;font-size:10px}
.tablet .section-label{right:4px;top:18px;font-size:9px}
.scroll{position:absolute;display:flex;flex-direction:column;align-items:center;color:var(--muted)}
.scroll span{writing-mode:vertical-rl}
.scroll i{width:0;height:0;border-left:4px solid transparent;border-right:4px solid transparent;border-top:7px solid var(--ink);margin-top:4px}
.desktop .scroll{right:10px;bottom:14px;font-size:10px}
.tablet .scroll{right:2px;bottom:12px;font-size:9px}
.dots{position:absolute;display:flex;flex-direction:column}
.dots i{display:block;width:3px;height:3px;border-radius:50%;background:#444;position:relative}
.dots i.on{width:5px;height:5px;margin-left:-1px;background:var(--ink)}
.dots i b{position:absolute;right:12px;top:-4px;font-weight:400;font-style:normal;font-size:9px;color:var(--muted);white-space:nowrap}
.desktop .dots{right:16px;gap:16px}
.tablet .dots{right:6px;gap:16px}
.phone .dots{flex-direction:row;left:0;width:178px;justify-content:center;gap:8px;top:167px}
.phone .dots i{width:2px;height:2px}
.phone .dots i.on{width:3px;height:3px;margin-left:0;margin-top:-.5px}

/* phone chrome */
.burger{position:absolute;right:8px;top:8px;width:9px;display:flex;flex-direction:column;gap:1.5px}
.burger i{display:block;height:1px;background:var(--ink)}
.crumb{position:absolute;left:4px;top:48px;font-size:5px;color:var(--muted)}
.phone-foot{position:absolute;left:0;bottom:0;width:178px;height:20px;background:var(--paper);display:flex;align-items:center;padding:0 4px;gap:5px;font-size:4.5px;line-height:1.1}
.phone-foot .nums{color:#444}
.phone-foot .round{width:9px;height:9px;border-radius:50%;background:var(--ink);margin-left:auto}
</style>
</head>
<body>
<svg width="0" height="0" style="position:absolute">
  <defs>
    <symbol id="phone" viewBox="0 0 24 24"><path d="M6.6 2.5l3 3.6-1.9 2.3c1.3 2.9 3.6 5.3 6.5 6.6l2.3-1.9 3.6 3-2.2 3.1C11 19 4.9 12.9 3.6 5.1z" fill="#1a1a1a"/></symbol>
    <symbol id="mail" viewBox="0 0 26 18"><rect x="1" y="1" width="24" height="16" fill="none" stroke="#1a1a1a" stroke-width="1.4"/><path d="M1 1l12 9 12-9M1 17l9-7M25 17l-9-7" fill="none" stroke="#1a1a1a" stroke-width="1.2"/></symbol>
  </defs>
</svg>

<main class="board">

<!-- ============ ROW 1 : VORSPEISEN ============ -->
<section class="screen desktop" style="left:143px;top:40px">
  <div class="brand"><span class="mark"></span>Elif Grillstube</div>
  <ul class="nav"><li>HOME</li><li>ELIF GRILLSTUBE</li><li><span class="boxed">CATERING</span></li><li>LIEFERSERVICE</li><li>MENU</li></ul>
  <div class="contact"><svg width="20" height="20"><use href="#phone"/></svg><div><p>Lieferservice &amp;<br>Catering:</p><p class="nums">02341 58220<br>01577 0921364</p></div></div>
  <div class="social"><span class="round"></span><svg width="24" height="17"><use href="#mail"/></svg></div>
  <div class="photo starters" role="img" aria-label="Foto: gefüllte Weinblätter, Börek und scharfe Paprikapaste"><h2 class="photo-title">VORSPEISEN</h2></div>
  <ul class="menu" style="top:92px;--gap:33px">
    <li><h3>10. Sigara Böregi<span>4,95€</span></h3><p>Mit Fetakäse gefüllte Blätterteigröllchen und dazu hausgemachte Joghurtcreme.</p></li>
    <li><h3>11. Elif Vorspeise<span>5,50€</span></h3><p>Frisch zubereitete und vielfältige Vorspeise mit türkischen Spezialitäten und frischen Gemüse.</p></li>
    <li><h3>12. Sarma<span>4,95€</span></h3><p>Gerollte und mit Reis gefüllte Weinblätter</p></li>
    <li><h3>13. Traditionelle Suppen<span>3,50€</span></h3><p>Linsensuppe, Pansensuppe und Hühnersuppe</p></li>
    <li><h3>14. Elif Frühstück<span>7,00€</span></h3><p>Unser besonderes, türkisch zubereitetes Frühstück inklusive Rührei, Sucuk, Käse und weiteren appetitlichen Zutaten</p></li>
  </ul>
  <p class="section-label">menu - speisen</p>
  <div class="dots" style="top:150px"><i class="on"><b>vorspeisen</b></i><i></i><i></i><i></i><i></i><i></i><i></i><i></i><i></i><i></i><i></i><i></i></div>
  <div class="scroll"><span>scroll down</span><i></i></div>
</section>

<section class="screen tablet" style="left:1137px;top:60px">
  <div class="brand"><span class="mark"></span>Elif Grillstube</div>
  <ul class="nav"><li>HOME</li><li>ELIF GRILLSTUBE</li><li><span class="boxed">CATERING</span></li><li>LIEFERSERVICE</li><li>MENU</li></ul>
  <div class="contact"><svg width="18" height="18"><use href="#phone"/></svg><div><p>Lieferservice &amp;<br>Catering:</p><p class="nums">02341 58220<br>01577 0921364</p></div></div>
  <div class="social"><span class="round"></span><svg width="22" height="15"><use href="#mail"/></svg></div>
  <div class="photo starters" role="img" aria-label="Foto: gefüllte Weinblätter, Börek und scharfe Paprikapaste"><h2 class="photo-title">VORSPEISEN</h2></div>
  <ul class="menu" style="top:252px;--gap:18px">
    <li><h3>10. Sigara Böregi<span>4,95€</span></h3><p>Mit Fetakäse gefüllte Blätterteigröllchen und dazu hausgemachte Joghurtcreme.</p></li>
    <li><h3>11. Elif Vorspeise<span>5,50€</span></h3><p>Frisch zubereitete und vielfältige Vorspeise mit türkischen Spezialitäten und frischen Gemüse.</p></li>
    <li><h3>12. Sarma<span>4,95€</span></h3><p>Gerollte und mit Reis gefüllte Weinblätter</p></li>
    <li><h3>13. Traditionelle Suppen<span>3,50€</span></h3><p>Linsensuppe, Pansensuppe und Hühnersuppe</p></li>
    <li><h3>14. Elif Frühstück<span>7,00€</span></h3><p>Unser besonderes Frühstück</p></li>
  </ul>
  <p class="section-label">menu - speisen</p>
  <div class="dots" style="top:146px"><i class="on"></i><i></i><i></i><i></i><i></i><i></i><i></i><i></i><i></i><i></i><i></i><i></i></div>
  <div class="scroll"><span>scroll down</span><i></i></div>
</section>

<section class="screen phone" style="left:1632px;top:247px">
  <div class="brand"><span class="mark"></span>Elif Grillstube</div>
  <div class="burger"><i></i><i></i><i></i></div>
  <p class="crumb">menu - speisen</p>
  <div class="photo starters" role="img" aria-label="Foto: gefüllte Weinblätter und Paprikapaste"><h2 class="photo-title">VORSPEISEN</h2></div>
  <div class="dots"><i class="on"></i><i></i><i></i><i></i><i></i><i></i><i></i><i></i><i></i><i></i><i></i><i></i></div>
  <ul class="menu" style="top:180px;--gap:6px">
    <li><h3>10. Sigara Böregi<span>4,95€</span></h3><p>Mit Fetakäse gefüllte Blätterteigröllchen und dazu hausgemachte Joghurtcreme.</p></li>
    <li><h3>11. Elif Vorspeise<span>5,50€</span></h3><p>Frisch zubereitete und vielfältige Vorspeise mit türkischen Spezialitäten und frischen Gemüse.</p></li>
    <li><h3>12. Sarma<span>4,95€</span></h3><p>Gerollte und mit Reis gefüllte Weinblätter</p></li>
    <li><h3>13. Traditionelle Suppen<span>3,50€</span></h3><p>Linsensuppe, Pansensuppe und Hühnersuppe</p></li>
  </ul>
  <div class="phone-foot"><svg width="8" height="8"><use href="#phone"/></svg><p>Lieferservice &amp;<br>Catering:</p><p class="nums">02341 58220<br>01577 0921364</p><span class="round"></span><svg width="10" height="7"><use href="#mail"/></svg></div>
</section>

<!-- ============ ROW 2 : PIZZEN ============ -->
<section class="screen desktop" style="left:143px;top:752px">
  <div class="brand"><span class="mark"></span>Elif Grillstube</div>
  <ul class="nav"><li>HOME</li><li>ELIF GRILLSTUBE</li><li><span class="boxed">CATERING</span></li><li>LIEFERSERVICE</li><li>MENU</li></ul>
  <div class="contact"><svg width="20" height="20"><use href="#phone"/></svg><div><p>Lieferservice &amp;<br>Catering:</p><p class="nums">02341 58220<br>01577 0921364</p></div></div>
  <div class="social"><span class="round"></span><svg width="24" height="17"><use href="#mail"/></svg></div>
  <div class="photo pizza" role="img" aria-label="Foto: türkische Pide-Pizza mit Chilischoten auf Holzbrett"><h2 class="photo-title">PIZZEN</h2></div>
  <ul class="menu" style="top:-6px;--gap:40px">
    <li><h3>110. Pizza Bella Margherita<span>4,80€</span></h3><p>Tomatensoße, Gouda.</p></li>
    <li><h3>111. Pizza Pomodoro<span>5,80€</span></h3><p>Tomatensoße, Gouda, Tomaten</p></li>
    <li><h3>112. Pizza Mediterrano<span>6,50€</span></h3><p>Tomatensoße, Gouda, Brokoli, Paprika, Oliven</p></li>
    <li><h3>113. Pizza Vegetaria<span>6,90€</span></h3><p>Tomatensoße, Gouda, Brokoli, Paprika, Spinat, Knoblauch</p></li>
    <li><h3>114. Pizza Sucuk<span>6,50€</span></h3><p>Tomatensoße, Gouda, Sucuk (türk. Knoblauchwurst)</p></li>
    <li><h3>115. Pizza Piccante<span>6,50€</span></h3><p>Tomatensoße, Gouda, Sucuk (türk. Knoblauchwurst), Jalapenos</p></li>
    <li><h3>116. Pizza Tonno<span>6,00€</span></h3><p>Tomatensoße, Gouda, Thunfisch</p></li>
    <li><h3>117. Pizza Funghi<span>6,00€</span></h3><p>Tomatensoße, Gouda, Champignons</p></li>
  </ul>
  <p class="section-label">menu - speisen</p>
  <div class="dots" style="top:150px"><i></i><i></i><i></i><i></i><i class="on"><b>pizzen</b></i><i></i><i></i><i></i><i></i><i></i><i></i><i></i></div>
  <div class="scroll"><span>scroll down</span><i></i></div>
</section>

<section class="screen tablet" style="left:1137px;top:772px">
  <div class="brand"><span class="mark"></span>Elif Grillstube</div>
  <ul class="nav"><li>HOME</li><li>ELIF GRILLSTUBE</li><li><span class="boxed">CATERING</span></li><li>LIEFERSERVICE</li><li>MENU</li></ul>
  <div class="contact"><svg width="18" height="18"><use href="#phone"/></svg><div><p>Lieferservice &amp;<br>Catering:</p><p class="nums">02341 58220<br>01577 0921364</p></div></div>
  <div class="social"><span class="round"></span><svg width="22" height="15"><use href="#mail"/></svg></div>
  <div class="photo pizza" role="img" aria-label="Foto: türkische Pide-Pizza mit Chilischoten"><h2 class="photo-title">PIZZEN</h2></div>
  <ul class="menu" style="top:252px;--gap:21px">
    <li><h3>110. Pizza Bella Margherita<span>4,80€</span></h3><p>Tomatensoße, Gouda.</p></li>
    <li><h3>111. Pizza Pomodoro<span>5,80€</span></h3><p>Tomatensoße, Gouda, Tomaten</p></li>
    <li><h3>112. Pizza Mediterrano<span>6,50€</span></h3><p>Tomatensoße, Gouda, Brokoli, Paprika, Oliven</p></li>
    <li><h3>113. Pizza Vegetaria<span>6,90€</span></h3><p>Tomatensoße, Gouda, Brokoli, Paprika, Spinat, Knoblauch</p></li>
    <li><h3>114. Pizza Sucuk<span>6,50€</span></h3><p>Tomatensoße, Gouda, Sucuk</p></li>
  </ul>
  <p class="section-label">menu - speisen</p>
  <div class="dots" style="top:146px"><i></i><i></i><i></i><i></i><i class="on"></i><i></i><i></i><i></i><i></i><i></i><i></i><i></i></div>
  <div class="scroll"><span>scroll down</span><i></i></div>
</section>

<section class="screen phone" style="left:1632px;top:959px">
  <div class="brand"><span class="mark"></span>Elif Grillstube</div>
  <div class="burger"><i></i><i></i><i></i></div>
  <p class="crumb">menu - speisen</p>
  <div class="photo pizza" role="img" aria-label="Foto: türkische Pide-Pizza"><h2 class="photo-title">PIZZEN</h2></div>
  <div class="dots"><i></i><i></i><i></i><i></i><i class="on"></i><i></i><i></i><i></i><i></i><i></i><i></i><i></i></div>
  <ul class="menu" style="top:180px;--gap:8px">
    <li><h3>110. Pizza Bella Margherita<span>4,80€</span></h3><p>Tomatensoße, Gouda.</p></li>
    <li><h3>111. Pizza Pomodoro<span>5,80€</span></h3><p>Tomatensoße, Gouda, Tomaten</p></li>
    <li><h3>112. Pizza Mediterrano<span>6,50€</span></h3><p>Tomatensoße, Gouda, Brokoli, Paprika, Oliven</p></li>
    <li><h3>113. Pizza Vegetaria<span>6,90€</span></h3><p>Tomatensoße, Gouda, Brokoli, Paprika, Spinat, Knoblauch</p></li>
  </ul>
  <div class="phone-foot"><svg width="8" height="8"><use href="#phone"/></svg><p>Lieferservice &amp;<br>Catering:</p><p class="nums">02341 58220<br>01577 0921364</p><span class="round"></span><svg width="10" height="7"><use href="#mail"/></svg></div>
</section>

<!-- ============ ROW 3 : ALKOHOLISCH ============ -->
<section class="screen desktop" style="left:143px;top:1464px">
  <div class="brand"><span class="mark"></span>Elif Grillstube</div>
  <ul class="nav"><li>HOME</li><li>ELIF GRILLSTUBE</li><li><span class="boxed">CATERING</span></li><li>LIEFERSERVICE</li><li>MENU</li></ul>
  <div class="contact"><svg width="20" height="20"><use href="#phone"/></svg><div><p>Lieferservice &amp;<br>Catering:</p><p class="nums">02341 58220<br>01577 0921364</p></div></div>
  <div class="social"><span class="round"></span><svg width="24" height="17"><use href="#mail"/></svg></div>
  <div class="photo drinks" role="img" aria-label="Foto: ein Glas Rotwein und ein Glas Bier auf Holztisch"><h2 class="photo-title">ALKEHOLISCH</h2></div>
  <ul class="menu" style="top:101px;--gap:40px">
    <li><h3>Kronfeld Pils &amp; Radler<span>2,40€</span></h3><p>330 ml</p></li>
    <li><h3>Ehrwald Weizenbier<span>3,00€</span></h3><p>0,5 l</p></li>
    <li><h3>Rotwein Villa Dolmaz<span>3,50€</span></h3><p>200 ml</p></li>
    <li><h3>Weisswein Villa Dolmaz<span>3,50€</span></h3><p>200 ml</p></li>
    <li><h3>Raki<span>2,00€</span></h3><p>2 cl</p></li>
  </ul>
  <p class="section-label">menu - getränke</p>
  <div class="dots" style="top:224px"><i></i><i class="on"><b>alkeholisch</b></i><i></i></div>
  <div class="scroll"><span>scroll down</span><i></i></div>
</section>

<section class="screen tablet" style="left:1137px;top:1484px">
  <div class="brand"><span class="mark"></span>Elif Grillstube</div>
  <ul class="nav"><li>HOME</li><li>ELIF GRILLSTUBE</li><li><span class="boxed">CATERING</span></li><li>LIEFERSERVICE</li><li>MENU</li></ul>
  <div class="contact"><svg width="18" height="18"><use href="#phone"/></svg><div><p>Lieferservice &amp;<br>Catering:</p><p class="nums">02341 58220<br>01577 0921364</p></div></div>
  <div class="social"><span class="round"></span><svg width="22" height="15"><use href="#mail"/></svg></div>
  <div class="photo drinks" role="img" aria-label="Foto: Rotwein und Bier auf Holztisch"><h2 class="photo-title">ALKEHOLISCH</h2></div>
  <ul class="menu" style="top:262px;--gap:26px">
    <li><h3>Kronfeld Pils &amp; Radler<span>2,40€</span></h3><p>330 ml</p></li>
    <li><h3>Ehrwald Weizenbier<span>3,00€</span></h3><p>0,5 l</p></li>
    <li><h3>Rotwein Villa Dolmaz<span>3,50€</span></h3><p>200 ml</p></li>
    <li><h3>Weisswein Villa Dolmaz<span>3,50€</span></h3><p>200 ml</p></li>
  </ul>
  <p class="section-label">menu - getränke</p>
  <div class="dots" style="top:216px"><i></i><i class="on"></i><i></i></div>
  <div class="scroll"><span>scroll down</span><i></i></div>
</section>

<section class="screen phone" style="left:1632px;top:1671px">
  <div class="brand"><span class="mark"></span>Elif Grillstube</div>
  <div class="burger"><i></i><i></i><i></i></div>
  <p class="crumb">menu - getränke</p>
  <div class="photo drinks" role="img" aria-label="Foto: Rotwein und Bier"><h2 class="photo-title">ALKEHOLISCH</h2></div>
  <div class="dots"><i></i><i class="on"></i><i></i></div>
  <ul class="menu" style="top:180px;--gap:10px">
    <li><h3>Kronfeld Pils &amp; Radler<span>2,40€</span></h3><p>330 ml</p></li>
    <li><h3>Ehrwald Weizenbier<span>3,00€</span></h3><p>0,5 l</p></li>
    <li><h3>Rotwein Villa Dolmaz<span>3,50€</span></h3><p>200 ml</p></li>
    <li><h3>Weisswein Villa Dolmaz<span>3,50€</span></h3><p>200 ml</p></li>
  </ul>
  <div class="phone-foot"><svg width="8" height="8"><use href="#phone"/></svg><p>Lieferservice &amp;<br>Catering:</p><p class="nums">02341 58220<br>01577 0921364</p><span class="round"></span><svg width="10" height="7"><use href="#mail"/></svg></div>
</section>

</main>
</body>
</html>
```